Cobalt Press website re-design

We would like to recreate the www.cobaltpress-demo.com.au website into a simpler and more sophisticated version. We want the buyer to be drawn to our site and establish that we are reputable and professional from the moment they enter. We want them to easily find the product or service they are looking for within our site, decide that they would like to find out more and either click through to obtain a quote or click through to contact a rep.

The current website has been created using MS Front Page, however we would like the newly designed site to be created in a mobile responsive WordPress CMS format

We are a Print Broker who can save clients time in hunting around for the right supplier for their print jobs. This is most likely appealing to larger organisations who haven’t got time to waste in finding quotes from many different suppliers for each type of job. We make it easy because we have access to a large network of trade only print & signage suppliers so we can select the best and most cost effective supplier depending on the type of print job. Further, because we don’t do the printing in-house we have low overheads which means we can ensure competitive prices.
Updates

Target Market(s)

Business owners, print managers, receptionists, marketing managers who are time poor, uneducated re:printing, after quick & cost effective solutions

Industry/Entity Type

Printing

Requirements
Must have
• Use the current logo and colours - see files uploaded
Limit scrolling and keep pages within view
Easy to see buttons that navigate the buyer through the site
The site is to be clear, easy to understand, free from clutter (ie.ensure white space) and have a Professional/corporate look
Easy to use Quotation forms
Imagery needs to be modern, and clean -see brightmarrow site

Competitor/other websites we like and why?
I like brightmarrow.com.au for its’ modern look. I like how the products are displayed in High resolution are very clean and uncluttered. You can easily find the product and access ‘get a quote’.
Pelham Print has a good layout for the quote request. Check out pelhamprint-demo.com.au
www.vendrak.com.au are print brokers/managers. Their descriptions are easy to understand but still heavy in content.
Nice to have
• 1. Home Page
½ page summary of the core business
Distinct buttons for products and services down the side (so that people can go straight to what they need.)
About Us (including profiles); Products and Services; Get a Quote; Contact us across the top

2. About Us
A brief overview of owner, staff and reps. Click through to Profiles for each region rep and contact details either as pop ups or separate pages.

3. Products and Services
Buttons or lists of products link to pop up with get a quote link within (this could be grouped such as Business Cards, Letterheads, Folders etc.; Club printing with plastic cards, sign in books, coasters etc.; Marketing such as flyers, posters, banners etc. (Note. look at how others have broken it up)
Include calling for advice for special products and finishes as service on how a job can be improved and done within budget.
4. Get a Quote
(2 sites mentioned below that I like for the get a quote system)

5. Contact Us
Clear sections divided by lines and details large starting with 1300 number
Head office
Regional numbers and areas they cover
Include emails.

Contact us now or click to request a rep contact you.

```html
<!DOCTYPE html>
<html lang="en">
<head>
<meta charset="utf-8">
<title>Cobalt Press — Printing, Signage, Display</title>
<link href="https://fonts.googleapis.com/css2?family=Mulish:wght@400;500;600;700;800&display=swap" rel="stylesheet">
<style>
:root{
  --brand-dark:#8b0010;
  --brand-red:#c8001a;
  --side-grey:#7b7b7b;
  --btn-grey:#8a8a8a;
  --btn-grey-dark:#6f6f6f;
  --text:#444;
  --text-light:#777;
  --nav:#777;
  --page:#ffffff;
}
*{margin:0;padding:0;box-sizing:border-box}
html,body{width:1200px;height:819px;overflow:hidden;background:var(--page)}
body{position:relative;font-family:"Mulish",Arial,sans-serif;color:var(--text)}
.abs{position:absolute}
.backdrop{left:0;top:0;width:1001px;height:819px;
  background:radial-gradient(ellipse 520px 300px at 500px 260px,#e9e9e9 0%,#f3f3f3 45%,#fff 80%)}
.side-grey{left:1001px;top:0;width:17px;height:819px;background:var(--side-grey)}
.side-red{left:1018px;top:0;width:182px;height:819px;background:var(--brand-dark)}
.call-tab{left:745px;top:8px;width:256px;height:32px;background:#8d8d8d;border-radius:4px 0 0 4px;display:flex;align-items:center;overflow:hidden}
.call-tab .icon{width:36px;height:32px;background:var(--brand-dark);display:flex;align-items:center;justify-content:center}
.call-tab .label{color:#fff;font-size:13px;padding-left:9px}
.call-tab .label b{font-size:16px;font-weight:700}
.logo{left:202px;top:44px;display:flex;align-items:center;gap:8px}
.logo .mark{width:60px;height:60px;background:var(--brand-dark);border-radius:7px}
.logo .name{font-size:17px;font-weight:800;color:var(--brand-dark)}
.main-nav{left:378px;top:83px;display:flex;font-size:13px;font-weight:600;color:var(--nav);letter-spacing:.2px}
.main-nav a{color:inherit;text-decoration:none;padding:0 17px;border-left:1px solid #ccc;line-height:16px}
.main-nav a:first-child{padding-left:0;border-left:0;color:var(--brand-dark)}
.hero-image{left:384px;top:164px;width:392px;height:192px;border-radius:3px;
  background:linear-gradient(100deg,#e8542a 0%,#f07a2c 40%,#f1efe9 55%,#e9d5cf 75%,#e48a60 100%)}
.arrow{top:279px}
.headline{left:0;width:1001px;top:374px;text-align:center;font-size:42px;font-weight:800;letter-spacing:-1.4px;color:#7f7f7f;padding-left:200px}
.headline .accent{color:var(--brand-dark)}
.headline .sep{font-weight:400;margin:0 12px}
.subtitle{left:0;width:1001px;top:427px;text-align:center;font-size:14.6px;color:#707070;padding-left:200px;letter-spacing:-.2px}
.tagline{left:268px;top:457px;font-size:9.4px;font-weight:500;color:#555;letter-spacing:0}
.panels{left:201px;top:512px;width:800px;height:235px;display:flex;background:linear-gradient(#fff,#ececec);box-shadow:0 10px 14px -10px rgba(0,0,0,.35);border-top:1px solid #ddd}
.panel{position:relative;width:200px;height:235px;border-left:1px solid #e2e2e2}
.panel:first-child{border-left:0}
.panel h2{font-size:13.8px;font-weight:600;color:var(--brand-dark);text-align:center;margin-top:21px;letter-spacing:-.3px;line-height:15px}
.panel h3{font-size:10px;font-weight:700;color:#333;text-align:center;line-height:13px}
.panel p{font-size:9.6px;line-height:13.4px;color:#555}
.welcome h2{text-align:left;font-size:24px;font-weight:800;margin:20px 0 0 23px;letter-spacing:-.2px}
.welcome p{position:absolute;left:8px;top:68px;width:188px}
.welcome p + p{top:135px}
.feature .thumb{position:absolute;left:32px;top:60px;width:120px;height:84px;background:linear-gradient(120deg,#d8dde6,#b7c0cc)}
.feature p{position:absolute;left:10px;top:146px;width:185px}
.quote p{position:absolute;left:15px;top:68px;width:178px}
.quote p + p{top:149px}
.clients .client-name{position:absolute;left:0;width:200px;top:117px;text-align:center;font-size:17px;font-weight:700;color:#555}
.cta{position:absolute;left:0;bottom:0;width:200px;height:33px;display:flex;align-items:center;justify-content:space-between;padding:0 22px 0 8px;color:#fff;font-size:12px;font-weight:600;text-decoration:none}
.cta.dark{background:var(--brand-dark)}
.cta.red{background:var(--brand-red)}
.cta.grey{background:var(--btn-grey);padding-left:16px}
.cta.grey-dark{background:var(--btn-grey-dark);padding-left:24px}
.footer-nav{left:201px;top:774px;font-size:9px;color:#555}
.copyright{left:201px;top:792px;font-size:10px;color:#999}
.social{left:898px;top:773px;display:flex;gap:5px}
.social span{width:13px;height:13px;background:#555;border-radius:2px}
</style>
</head>
<body>
<div class="abs backdrop"></div>
<div class="abs side-grey"></div>
<div class="abs side-red"></div>

<div class="abs call-tab">
  <div class="icon">
    <svg width="16" height="16" viewBox="0 0 24 24"><path fill="#fff" d="M6.6 10.8a15.1 15.1 0 0 0 6.6 6.6l2.2-2.2a1 1 0 0 1 1-.25 11.4 11.4 0 0 0 3.6.57 1 1 0 0 1 1 1V20a1 1 0 0 1-1 1A17 17 0 0 1 3 4a1 1 0 0 1 1-1h3.5a1 1 0 0 1 1 1c0 1.250.2 2.45.57 3.57a1 1 0 0 1-.25 1z"/></svg>
  </div>
  <div class="label">Call Us Today: <b>1300 555 019</b></div>
</div>

<div class="abs logo"><span class="mark"></span><span class="name">Cobalt Press</span></div>

<nav class="abs main-nav">
  <a href="#">HOME</a><a href="#">ABOUT US</a><a href="#">PRODUCTS &amp; SERVICES</a><a href="#">GET A QUOTE</a><a href="#">CONTACT US</a>
</nav>

<div class="abs hero-image" role="img" aria-label="Photo of a printed hardcover art book with an orange abstract cover beside an open book"></div>

<svg class="abs arrow" style="left:202px" width="14" height="20" viewBox="0 0 14 20"><path d="M11 2 3 10l8 8" fill="none" stroke="#666" stroke-width="2.5"/></svg>
<svg class="abs arrow" style="left:971px" width="14" height="20" viewBox="0 0 14 20"><path d="M3 2l8 8-8 8" fill="none" stroke="#666" stroke-width="2.5"/></svg>

<h1 class="abs headline">Printing<span class="sep">|</span><span class="accent">Signage</span><span class="sep">|</span>Display</h1>
<div class="abs subtitle">YOUR COMMERCIAL PRINTING &amp; SIGNAGE SPECIALIST</div>
<div class="abs tagline">LOW COST &nbsp;-&nbsp; LATEST TECHNOLOGY &nbsp;-&nbsp; FAST TURNAROUND PREMIUM QUALITY &nbsp;-&nbsp; FROM AUSTRALIA’S LEADING SPECIALIST TRADE SUPPLIERS</div>

<section class="abs panels">
  <div class="panel welcome">
    <h2>WELCOME</h2>
    <p>Using Australia’s leading print trade suppliers, we provide our clients with the most cost effective print solution in the market.</p>
    <p>We are constantly sourcing the most advanced technology in the industry to produce the lowest unit price, best quality and fastest Australia wide delivery.</p>
    <a class="cta dark" href="#">View More Details<span>✚</span></a>
  </div>
  <div class="panel feature">
    <h2>NEW PRODUCT FEATURE</h2>
    <h3>CRYSTAL VARNISH</h3>
    <div class="thumb" role="img" aria-label="Photo of three printed cards finished with crystal varnish"></div>
    <p>Crystal Varnish is an exclusive NEW UV finish achieving a matt &amp; gloss UV on the one surface in one pass at perfect registration...</p>
    <a class="cta red" href="#">View More Details<span>✚</span></a>
  </div>
  <div class="panel quote">
    <h2>ASK FOR A QUOTE</h2>
    <h3>JUST A CLICK AWAY</h3>
    <p>From small run digital, to offset, wide-format, signage, packaging, point of sale or specialist hotel, retail &amp; club supplies our product knowledge is second to none.</p>
    <p>Call 1300 555 019 to discuss your job or ask us for a quote.</p>
    <a class="cta grey" href="#">Ask For A QUOTE<span>✚</span></a>
  </div>
  <div class="panel clients">
    <h2>OUR CLIENTS</h2>
    <h3>AUSTRALIA’S BIGGEST NAMES</h3>
    <div class="client-name">Meridian Freight</div>
    <a class="cta grey-dark" href="#">View More Clients<span>✚</span></a>
  </div>
</section>

<div class="abs footer-nav">HOME - ABOUT US - PRODUCTS &amp; SERVICES - GET A QUOTE - CONTACT US</div>
<div class="abs copyright">© 2013 Cobalt Press &nbsp;A Division of Southern Trade Buying Group Pty Limited. All rights reserved.</div>
<div class="abs social" aria-label="Social links"><span></span><span></span><span></span><span></span><span></span></div>
</body>
</html>
```